New Book Cover for Website Advertising

I need a new book cover design to go on my website to generate pre-orders before my book is published. I have a previous design which I think needs a refresh. I want the new cover to complement the colours of my new website and logo. I'll attach the old book cover. All the words will remain the same, I just need an entirely new design

Target Market(s)

Corporate Leaders

Industry/Entity Type

Human resources

Font styles to use
Sans Serif

Colors
F0912C
F2A743
F7CA91
FBE8D2
FDF5EE
6B429C
8869AF
B7A5CE
E3DAEB
F3F0F8

Requirements
Must have
• A feeling of lightness, not dark
Should not have
• Any clip art or common stock photos

```html
<!DOCTYPE html>
<html lang="en">
<head>
<meta charset="utf-8">
<title>The Secure Leader – Book Cover</title>
<link href="https://fonts.googleapis.com/css2?family=Bebas+Neue&family=Oswald:wght@400&display=swap" rel="stylesheet">
<style>
  :root {
    --backdrop: #dedede;
    --orange: #f0912c;
    --orange-mid: #f2a743;
    --orange-soft: #f7ca91;
    --orange-pale: #fbe8d2;
    --cream: #fdf5ee;
    --purple: #6b429c;
    --purple-mid: #8869af;
    --purple-soft: #b7a5ce;
    --purple-pale: #e3daeb;
    --lilac: #f3f0f8;
  }
  html, body {
    margin: 0;
    width: 1200px;
    height: 1200px;
    overflow: hidden;
    background: var(--backdrop);
  }
  .book-cover {
    position: absolute;
    left: 210px;
    top: 30px;
    width: 780px;
    height: 1140px;
    overflow: hidden;
    background: var(--cream);
  }
  .cover-photo {
    position: absolute;
    inset: 0;
    background:
      linear-gradient(180deg, var(--lilac) 0%, rgba(243,240,248,0) 14%),
      linear-gradient(100deg, var(--orange-pale) 0%, var(--cream) 38%, var(--purple-pale) 62%, var(--purple-soft) 100%);
  }
  .title {
    margin: 0;
  }
  .title-line {
    position: absolute;
    left: 29px;
    font-family: "Bebas Neue", sans-serif;
    font-weight: 400;
    line-height: 0.72;
    white-space: nowrap;
  }
  .title-the    { top: 274px; font-size: 146px; color: var(--purple); }
  .title-secure { top: 400px; font-size: 174px; color: var(--purple); }
  .title-leader { top: 540px; font-size: 196px; color: var(--orange); }
  .subtitle {
    position: absolute;
    left: 44px;
    top: 734px;
    margin: 0;
    font-family: "Bebas Neue", sans-serif;
    font-size: 30px;
    line-height: 34.5px;
    color: var(--purple);
    letter-spacing: 0.3px;
  }
  .subtitle .highlight { color: var(--orange); }
  .author {
    position: absolute;
    left: 0;
    right: 0;
    top: 1034px;
    margin: 0;
    text-align: center;
    padding-left: 14px;
    font-family: "Oswald", sans-serif;
    font-weight: 400;
    font-size: 56px;
    line-height: 1;
    letter-spacing: 14px;
    color: var(--purple);
  }
</style>
</head>
<body>
  <main class="book-cover">
    <div class="cover-photo" role="img" aria-label="Photo of a businessman in a suit with arms crossed, a cape billowing behind him against a pale sky"></div>
    <h1 class="title">
      <span class="title-line title-the">THE</span>
      <span class="title-line title-secure">SECURE</span>
      <span class="title-line title-leader">LEADER</span>
    </h1>
    <p class="subtitle">DISCOVER HOW YOU<br>ATTACHMENT STYLE <span class="highlight">IMPACTS</span><br><span class="highlight">RELATIONSHOP</span> WITH YOUR<br>TEAM MEMBERS, AND THEIR<br>WELLBEING AND<br>PERFORMANCE</p>
    <p class="author">MAREN HOLT</p>
  </main>
</body>
</html>
```